Marlow Optics PowerPoint Template

Marlow Optics needs a nice new corporate PowerPoint template, to be used for all types of presentations: sales, business development, finance, board/exec, etc.

I'd like to get a clean layout that reflects the brand (www.marlowoptics.example), has a bright, interesting title slide, and then minimal graphics on the content slides. Ideally the content slides would have a header, "mo" circle part of the Marlow Optics logo (either above or below), copyright/confidential footer, and page #.

About us: we have developed a revolutionary new array camera for mobile devices, providing depth at every pixel. Focus on any subject, change focus (even on multiple subjects) after you take the photo, capture linear measurements, scale and segment your images, change backgrounds, and apply filters, all from any device.
It's not just about megapixels anymore.
See www.marlowoptics.example for info.

Target Market(s)

The audience for 90% of our presentations is highly educated executives at technology companies.

Industry/Entity Type

Camera

Requirements
Nice to have
• It would be great to show an image in a phone UI on the title slide, similar to the approach on our website.
Helpful to have tagline on title slide: "A smart camera for your smartphone." It may also fit on the content slides - feel free to try.
I attached a product photo, but using it is completely optional.
I'd like the "mo" circle on the content slides, but the whole logo on the title slides.
Thanks!

```html
<!DOCTYPE html>
<html lang="en">
<head>
<meta charset="utf-8">
<title>Marlow Optics – Presentation Template</title>
<link href="https://fonts.googleapis.com/css2?family=Titillium+Web:wght@200;300;400;600;700&family=Satisfy&display=swap" rel="stylesheet">
<style>
  :root {
    --page: #ffffff;
    --panel: #dcdcdc;
    --slide: #ffffff;
    --red-dark: #7a0e1b;
    --red: #a9222f;
    --red-light: #c13a47;
    --teal: #1b8ea4;
    --teal-dark: #0c5869;
    --navy: #173f5c;
    --ink: #3a3a3a;
    --muted: #8a8a8a;
    --line: #cfcfcf;
    --accent-blue: #1f88a8;
    --night: #12394f;
    --night-deep: #0b2a3c;
    --sky: #9fd3ea;
  }
  * { box-sizing: border-box; margin: 0; padding: 0; }
  html, body { width: 1200px; height: 3032px; overflow: hidden; }
  body { background: var(--page); font-family: "Titillium Web", sans-serif; color: var(--ink); position: relative; }

  .panel { position: absolute; left: 25px; top: 25px; width: 1150px; height: 2982px; background: var(--panel); border-radius: 22px; }

  .slide { position: absolute; left: 144px; width: 917px; height: 652px; background: var(--slide); overflow: hidden; box-shadow: 0 4px 12px rgba(0,0,0,.25); }
  .slide--title { top: 126px; }
  .slide--chart { top: 834px; }
  .slide--map { top: 1546px; }
  .slide--closing { top: 2248px; }

  .header-band { position: absolute; left: 0; top: 0; width: 917px; height: 160px; }

  .photo { position: absolute; left: 0; top: 0; width: 100%; height: 100%; }
  .photo--warm { background: linear-gradient(160deg, #e8e2d6 0%, #c7b7a0 40%, #8f6c52 70%, #b9a893 100%); }
  .photo--night { background: linear-gradient(170deg, #1d5068 0%, var(--night) 45%, var(--night-deep) 100%); }

  .brand { position: absolute; display: flex; align-items: center; gap: 10px; color: #fff; }
  .brand__dot { width: 36px; height: 36px; border-radius: 50%; background: #fff; }
  .brand__name { font-size: 32px; font-weight: 600; line-height: 1; }
  .brand--title { left: 628px; top: 62px; }

  .badge { position: absolute; left: 106px; top: 48px; display: flex; align-items: center; gap: 10px; }
  .badge__dot { width: 62px; height: 62px; border-radius: 50%; background: #fff; border: 4px solid var(--navy); }
  .badge__text { color: #fff; font-size: 26px; font-weight: 600; }

  .section-label { position: absolute; right: 110px; top: 48px; color: #fff; font-weight: 200; font-size: 50px; line-height: 1; letter-spacing: 1px; }

  .tagline { position: absolute; left: 190px; top: 598px; font-family: "Satisfy", cursive; font-size: 28px; letter-spacing: 4px; color: #fff; }
  .tagline--blue { color: var(--sky); }

  .main-title { position: absolute; left: 88px; color: var(--navy); font-weight: 700; font-size: 33px; line-height: 1; }
  .slide--chart .main-title { top: 245px; }
  .slide--map .main-title { top: 263px; }

  .block { position: absolute; font-size: 15px; line-height: 20px; color: var(--ink); }
  .block__head { color: var(--red); font-weight: 600; font-size: 16px; margin-bottom: 2px; }
  .block__note { color: var(--accent-blue); font-weight: 700; }

  .callout { position: absolute; left: 690px; width: 200px; font-size: 11px; line-height: 13px; color: var(--muted); }
  .callout__head { color: var(--navy); font-weight: 700; font-size: 13px; }
  .callout__pct { color: var(--red); font-size: 24px; font-weight: 700; }

  .footer { position: absolute; left: 88px; top: 618px; font-size: 10px; letter-spacing: 3px; color: var(--muted); text-transform: uppercase; }
  .footer strong { color: var(--red); font-weight: 600; }
  .page-no { position: absolute; right: 46px; top: 618px; font-size: 10px; letter-spacing: 2px; color: var(--muted); }
  .page-no strong { color: var(--red); }

  .chart-photo { position: absolute; left: 683px; top: 342px; width: 100px; height: 100px; border-radius: 50%; background: radial-gradient(circle, #d9d2c8, #7f6757); }

  .map { position: absolute; left: 322px; top: 180px; width: 514px; height: 188px; background: linear-gradient(180deg, #e6e9ec, #d6dbe0); border-radius: 6px; }

  .contact { position: absolute; right: 70px; top: 165px; text-align: right; color: #d6e6ee; font-size: 20px; line-height: 26px; font-weight: 300; }
  .contact p { margin-bottom: 22px; }
  .contact__web { color: var(--sky); font-weight: 600; }
  .contact svg { vertical-align: -3px; margin-left: 6px; }
</style>
</head>
<body>
<div class="panel"></div>

<svg width="0" height="0" style="position:absolute">
  <defs>
    <linearGradient id="band-red" x1="0" x2="1" y1="0" y2="0">
      <stop offset="0" stop-color="#6f0c18"/>
      <stop offset="1" stop-color="#b32c3a"/>
    </linearGradient>
    <linearGradient id="band-teal" x1="0" x2="1" y1="0" y2="0">
      <stop offset="0" stop-color="#1b93aa"/>
      <stop offset="1" stop-color="#116a7e"/>
    </linearGradient>
    <symbol id="header" viewBox="0 0 917 160">
      <polygon points="121,38 838,38 868,82 838,126 121,126" fill="url(#band-red)"/>
      <polygon points="0,30 104,30 104,134 0,134" fill="url(#band-teal)"/>
      <polygon points="104,30 121,38 121,126 104,134" fill="#0b4d5c"/>
    </symbol>
  </defs>
</svg>

<!-- Title slide -->
<section class="slide slide--title">
  <div class="photo photo--warm" role="img" aria-label="Photo of a smiling man framing a shot with a smartphone held in both hands, city skyline behind"></div>
  <svg class="header-band"><use href="#header"/></svg>
  <div class="brand brand--title"><span class="brand__dot"></span><span class="brand__name">Marlow Optics</span></div>
  <p class="tagline">a smart camera for your smartphone</p>
</section>

<!-- Content slide: chart -->
<section class="slide slide--chart">
  <svg class="header-band"><use href="#header"/></svg>
  <div class="badge"><span class="badge__dot"></span><span class="badge__text">mo</span></div>
  <h2 class="section-label">FINANCE</h2>
  <h1 class="main-title">Main Title</h1>

  <svg style="position:absolute;left:0;top:0" width="917" height="652">
    <circle cx="80" cy="335" r="4" fill="var(--red)"/>
    <polyline points="80,335 645,335 695,300" fill="none" stroke="var(--line)" stroke-width="1.5"/>
    <polyline points="680,232 660,232 660,280 695,315" fill="none" stroke="var(--line)" stroke-width="1.5"/>
    <polyline points="695,470 660,510 660,552 680,552" fill="none" stroke="var(--line)" stroke-width="1.5"/>
    <circle cx="680" cy="232" r="4" fill="var(--red)"/>
    <circle cx="680" cy="552" r="4" fill="var(--red)"/>
    <circle cx="733" cy="392" r="75" fill="var(--red)"/>
    <path d="M733 392 L733 317 A75 75 0 0 1 804 415 Z" transform="rotate(115 733 392)" fill="var(--teal-dark)"/>
    <circle cx="733" cy="392" r="56" fill="#f0e6e3"/>
  </svg>
  <div class="chart-photo" role="img" aria-label="Phone screen showing a captured photo"></div>

  <div class="callout" style="top:200px"><span class="callout__pct">70%</span> <span class="callout__head">Nulla Delectus</span><br>Eam oratio utinam minimum ei, usu id solet alienum pertinacia.</div>
  <div class="callout" style="top:525px"><span class="callout__pct">30%</span> <span class="callout__head">Insolens Rependunt</span><br>No tempor delectus assentior eam, pri sale clita quidam.</div>

  <div class="block" style="left:88px;top:318px;width:470px">
    <p class="block__head">Eam oratio utinam</p>
    <p>Nulla delectus cu nam, per insolens reprehendunt te. No tempor delectus assentior eam, pri sale clita quidam ex. Eam oratio utinam minimum ei, usu id solet alienum pertinacia.</p>
  </div>
  <div class="block" style="left:88px;top:430px;width:470px">
    <p class="block__head">Tamquam prompta</p>
    <p>Eros aeque corpora eum ex, laoreet iudicabit posidonium quo te. Mei ex legere civibus phaedrum. Id eam putent conceptam. Tamquam prompta an eos, ad libris placerat vix, ius eu phaedrum necessitatibus. Ad malis nihil epicurei mei.</p>
  </div>

  <p class="footer">Marlow Optics &nbsp;|&nbsp; <strong>Copyright 2015</strong></p>
  <p class="page-no"><strong>03</strong> | 15</p>
</section>

<!-- Content slide: map -->
<section class="slide slide--map">
  <svg class="header-band"><use href="#header"/></svg>
  <div class="badge"><span class="badge__dot"></span><span class="badge__text">mo</span></div>
  <h2 class="section-label">FINANCE</h2>
  <div class="map" role="img" aria-label="Dotted world map with location markers"></div>
  <h1 class="main-title">Main Title</h1>

  <svg style="position:absolute;left:0;top:0" width="917" height="652">
    <circle cx="80" cy="384" r="4" fill="var(--red)"/>
    <line x1="80" y1="384" x2="836" y2="384" stroke="var(--line)" stroke-width="1.5"/>
  </svg>

  <div class="block" style="left:88px;top:404px;width:380px">
    <p class="block__head">Eam oratio utinam</p>
    <p>Nulla delectus cu nam, per insolens repre hendunt te. No tempor delectus assentior eam, pri sale clita quidam ex.</p>
    <p class="block__note">Tamquam prompta an eos, ad libris placerat vix, ius eu phaedrum necessitatibus.</p>
  </div>
  <div class="block" style="left:523px;top:404px;width:340px">
    <p class="block__head">Eam oratio utinam</p>
    <p>Eros aeque corpora eum ex, laoreet iudicabit posidonium quo te. Mei ex legere civibus phaedrum. Id eam putent conceptam.</p>
    <p class="block__note">Tamquam prompta an eos, ad libris placerat vix, ius eu phaedrum necessitatibus. Ad malis nihil epicurei mei.</p>
  </div>

  <p class="footer">Marlow Optics &nbsp;|&nbsp; <strong>Copyright 2015</strong></p>
  <p class="page-no"><strong>03</strong> | 15</p>
</section>

<!-- Closing slide -->
<section class="slide slide--closing">
  <div class="photo photo--night" role="img" aria-label="Dark blue tinted photo of a man taking a picture with a smartphone"></div>
  <svg class="header-band"><use href="#header"/></svg>
  <div class="brand brand--title"><span class="brand__dot"></span><span class="brand__name">Marlow Optics</span></div>
  <div class="contact">
    <p>218 Harbor Lane<svg width="14" height="18" viewBox="0 0 14 18"><path d="M7 0a7 7 0 0 0-7 7c0 5 7 11 7 11s7-6 7-11a7 7 0 0 0-7-7zm0 10a3 3 0 1 1 0-6 3 3 0 0 1 0 6z" fill="currentColor"/></svg><br>Lakemont, OR 97035 USA</p>
    <p>1 (555) 014-2290<svg width="16" height="16" viewBox="0 0 16 16"><path d="M3 1l3 3-2 2c1 2 3 4 5 5l2-2 3 3-2 3C7 15 1 9 1 3z" fill="currentColor"/></svg><br>info@marlowoptics.example <span>@</span></p>
    <p class="contact__web">www.marlowoptics.example</p>
  </div>
  <p class="tagline tagline--blue">a smart camera for your smartphone</p>
</section>
</body>
</html>
```